" Nosso escritório de advocacia atende a empresas diversas, oferecendo serviços de consultoria na área trabalhista, orientação para defesa em fiscalizações, defesas em processos administrativos e judiciais trabalhistas, sempre focado no cuidado com as necessidades pessoais dos clientes e do seu patrimônio. "

```html
<!DOCTYPE html>
<html lang="pt-BR">
<head>
<meta charset="utf-8">
<title>Barreto Lima Souza Advocacia — Cartão de visita</title>
<link href="https://fonts.googleapis.com/css2?family=Marcellus&display=swap" rel="stylesheet">
<style>
  :root {
    --navy: #16304d;
    --ink: #2b3f57;
    --icon: #4d6580;
    --paper: #ffffff;
    --backdrop: #eef0f2;
  }
  * { margin: 0; padding: 0; box-sizing: border-box; }
  html, body { width: 1200px; height: 1200px; overflow: hidden; }
  body {
    background: var(--backdrop);
    font-family: "Marcellus", serif;
    position: relative;
  }
  .card {
    position: absolute;
    left: 180px;
    width: 840px;
    height: 536px;
    overflow: hidden;
  }
  .card--front { top: 60px; background: var(--navy); }
  .card--back { top: 624px; background: var(--paper); border: 1px solid #dde1e6; }

  .wordmark { position: absolute; text-align: center; font-weight: 400; }
  .wordmark__initials { display: block; letter-spacing: 0.08em; line-height: 1; }
  .wordmark__names { display: block; letter-spacing: 0.04em; text-transform: uppercase; }
  .wordmark__office { display: block; letter-spacing: 0.55em; text-transform: uppercase; }

  .card--front .wordmark {
    color: var(--paper);
    left: 0; right: 0; top: 170px;
  }
  .card--front .wordmark__initials { font-size: 120px; }
  .card--front .wordmark__names { font-size: 28px; margin-top: 14px; }
  .card--front .wordmark__office { font-size: 19px; margin-top: 8px; padding-left: 0.55em; }

  .card--back .wordmark {
    color: var(--ink);
    left: 100px; top: 150px; width: 240px;
  }
  .card--back .wordmark__initials { font-size: 78px; }
  .card--back .wordmark__names { font-size: 13px; margin-top: 10px; }
  .card--back .wordmark__office { font-size: 10px; margin-top: 4px; padding-left: 0.55em; }

  .holder {
    position: absolute;
    left: 440px; width: 340px; top: 167px;
    text-align: center;
    color: var(--ink);
    font-size: 21px;
    line-height: 36px;
  }
  .contacts {
    position: absolute;
    left: 406px; top: 306px;
    list-style: none;
    color: var(--ink);
    font-size: 19px;
  }
  .contacts li { display: flex; align-items: center; height: 36px; white-space: nowrap; }
  .contacts svg { width: 22px; height: 22px; margin-right: 10px; flex: none; }
  .contacts .phone { letter-spacing: 0.32em; }
  .contacts .web { letter-spacing: 0.1em; }
</style>
</head>
<body>

<section class="card card--front" aria-label="Frente do cartão">
  <div class="wordmark">
    <span class="wordmark__initials">BLS</span>
    <span class="wordmark__names">Barreto | Lima | Souza</span>
    <span class="wordmark__office">Advocacia</span>
  </div>
</section>

<section class="card card--back" aria-label="Verso do cartão">
  <div class="wordmark">
    <span class="wordmark__initials">BLS</span>
    <span class="wordmark__names">Barreto | Lima | Souza</span>
    <span class="wordmark__office">Advocacia</span>
  </div>

  <div class="holder">
    <p class="holder__name">Nome Sobrenome</p>
    <p class="holder__role">Cargo</p>
  </div>

  <ul class="contacts">
    <li>
      <svg viewBox="0 0 24 24" fill="none" stroke="var(--icon)" stroke-width="1.6"><rect x="2" y="5" width="20" height="14"/><path d="M2 5l10 8 10-8"/></svg>
      <span>Ononoonon onon on nono, 999</span>
    </li>
    <li>
      <svg viewBox="0 0 24 24"><rect x="1" y="1" width="22" height="22" rx="3" fill="var(--icon)"/><path d="M8 6c-1 0-2 1-2 2 0 5 5 10 10 10 1 0 2-1 2-2l-3-2-1.5 1.5c-2-1-3-2-4-4L11 10 9 6z" fill="#fff"/></svg>
      <span class="phone">(99) 9999-9999</span>
    </li>
    <li>
      <svg viewBox="0 0 24 24" fill="none" stroke="var(--icon)" stroke-width="1.6"><rect x="7" y="2" width="10" height="20" rx="2"/><path d="M11 18.5h2"/></svg>
      <span class="phone">(99) 9999-9999</span>
    </li>
    <li>
      <svg viewBox="0 0 24 24" fill="none" stroke="var(--icon)" stroke-width="1.8"><circle cx="12" cy="12" r="4"/><path d="M16 8v5.5c0 1.5 1 2.5 2.5 2.5S21 14.5 21 12a9 9 0 1 0-4 7.5"/></svg>
      <span>contato@blsadvocacia.com.br</span>
    </li>
    <li>
      <svg viewBox="0 0 24 24" fill="none" stroke="var(--icon)" stroke-width="1.6"><rect x="4" y="5" width="16" height="11"/><path d="M1 19h22"/></svg>
      <span class="web">www.blsadvocacia.com.br</span>
    </li>
  </ul>
</section>

</body>
</html>
```